Industrial Company Profile Brochure Design

We need company profile brochure design. We are in industrial valve business and we are serving oil, petrochemical and power plants. We are working with our clients as trusted advisor. So, the final design should communicate valve solutions expert. The brochure should be 4 pages (including front and back) or folded style. However, it is open. We do not like to put any restriction on creativity. We leave the decision for number of pages and page size to the designer. The color theme should be same as / compatible with logo colors. You should use icons.Find attached the followings:- Our Logo- Word file that contains the required content (text and photos) for the brochure.3 Modern brochure designs. We like these designs. This is just to give you idea about what we like. The brochure is simple, clear and easy to get full information quickly.- Just banner for valve and components. You may need it.

Target Market(s)

The end users of oi, petrochemical and power plants

Industry/Entity Type

Engineering Consulting

Requirements
Must have
• - You must add our slogan. It is "Your Valves Solutions Expert"

```html
<!DOCTYPE html>
<html lang="en">
<head>
<meta charset="utf-8">
<title>Norvale Advisory – Company Profile Spread</title>
<link href="https://fonts.googleapis.com/css2?family=Montserrat:wght@400;500;600&display=swap" rel="stylesheet">
<style>
  :root{
    --bg:#323232;
    --page:#f1f1f1;
    --page-shade:#e4e4e4;
    --ink:#1e1e1e;
    --body:#3a3a3a;
    --accent:#f0931e;
    --photo-steel:#b9bcc0;
    --photo-dark:#7d7a72;
    --photo-wall:#d8d6d0;
  }
  *{box-sizing:border-box;margin:0;padding:0}
  html,body{width:1200px;height:833px;overflow:hidden;background:var(--bg)}
  body{font-family:'Montserrat',sans-serif;color:var(--body)}
  .spread{position:absolute;left:50px;top:36px;width:1100px;height:760px;display:flex;box-shadow:0 10px 30px rgba(0,0,0,.45)}
  .page{position:relative;width:550px;height:760px;overflow:hidden;border-bottom:4px solid var(--accent)}
  .page--left{background:linear-gradient(90deg,#f7f7f7 0%,var(--page) 85%,#d9d9d9 100%)}
  .page--right{background:linear-gradient(90deg,#d6d6d6 0%,var(--page) 12%,#f6f6f6 100%)}
  .page-inner{position:absolute;left:48px;top:40px;right:44px}
  .page--right .page-inner{top:36px}
  .section-title{font-size:20px;font-weight:500;letter-spacing:1.5px;text-transform:uppercase;color:var(--ink);margin:0 0 10px}
  .section-title .hl{color:var(--accent)}
  .sub-title{font-size:15px;font-weight:500;color:var(--ink);margin:10px 0 5px}
  .sub-title .hl{color:var(--accent)}
  p{font-size:9.6px;line-height:1.45;margin-bottom:6px}
  .narrow{width:268px}
  .beside-photo{width:286px}
  .ticks{list-style:none;margin:4px 0 6px}
  .ticks li{font-size:9.6px;line-height:1.55;padding-left:16px;position:relative}
  .ticks li svg{position:absolute;left:0;top:3px}
  .lead-accent{font-size:11px;color:var(--accent);line-height:1.4;margin:6px 0 2px;width:270px}
  .photo{position:absolute}
  .photo--actuator{right:44px;top:262px;width:180px;height:110px;background:linear-gradient(135deg,#fafafa,var(--photo-steel) 60%,#e9e9e9)}
  .photo--trim{right:44px;top:382px;width:180px;height:120px;background:linear-gradient(135deg,#9a958a,var(--photo-dark) 50%,#c9c3b5)}
  .photo--valve{right:40px;top:292px;width:172px;height:200px;background:linear-gradient(180deg,var(--photo-wall) 0%,#c9cccd 45%,#6b7072 75%,#a58a66 100%)}
  .photo--ring{right:40px;top:502px;width:172px;height:60px;background:linear-gradient(180deg,#ececec,#cfcfcf)}
  .photo--parts{right:40px;top:570px;width:172px;height:100px;background:linear-gradient(135deg,#e2e2e2,#a9abad 55%,#d4d4d4)}
  .strategy{margin-top:16px}
  .solutions-title{margin-top:24px}
</style>
</head>
<body>
<main class="spread">
  <section class="page page--left">
    <div class="page-inner">
      <h2 class="section-title">About <span class="hl">Us</span></h2>
      <p>Norvale Advisory was established to provide highly-reliable consultation services for a selection of valve designs for various industrial applications. We specialize in recommending new valves for different types of industrial needs, as well as re-engineering the obsolete and troublesome ones, to provide technologically-advanced replacements.</p>
      <p>The key to the company’s success is the maintenance of a close working relationship with the clients. This is accomplished by ensuring the best possible solutions for their needs in order to establish and maintain a thorough knowledge and understanding of clients’ objectives, helping maximize the benefits.</p>
      <p>We at Norvale Advisory are a group of enthusiastic professionals who take pride in providing quality products to our clients. We help them find the best solutions for their needs by providing highly-experienced consultation services.</p>

      <h2 class="section-title" style="margin-top:14px">Company <span class="hl">Values</span></h2>
      <p class="narrow">At Norvale Advisory, we are committed to providing the best solutions to our clients and improving our skill sets and technology to deliver high-quality valves and valve components.</p>
      <h3 class="sub-title">Our <span class="hl">Vision</span></h3>
      <p class="narrow">To become the most trusted valve advisor in the region, maintaining the integrity and reliability of our services among our clients.</p>
      <h3 class="sub-title">Our <span class="hl">Mission</span></h3>
      <p class="narrow">To cooperate with our clients in finding the most reliable and cost-effective solutions for their valve-related requirements.</p>

      <div class="strategy">
        <h2 class="section-title">Strategic <span class="hl">Approach</span></h2>
        <p>The most important aspect of the solutions provided by us is that we deliver tailor-fit designs to accurately and effectively meet the needs that are not well-served by the valves currently available in the market. As in current valve manufacturing companies, the engineers are limited to providing standard designs created by their companies. This also limits them from fulfilling any type of modification requirement. For this reason, there are many valve problems that cannot be solved by standard designs. Furthermore, the parts replacements provided by us meet the requirements and come at a much lower cost, as compared to the parts delivered by these manufacturers.</p>
        <p>We are open and cooperate with several trusted companies to find the best solutions for the end-user problems by providing detailed analysis and consultation services, helping them to buy the most relevant products as per their needs. We aim to be the best choice in valve consultation.</p>
      </div>
    </div>
    <div class="photo photo--actuator" role="img" aria-label="Photo of an electric valve actuator unit"></div>
    <div class="photo photo--trim" role="img" aria-label="Photo of machined valve cage and trim components"></div>
  </section>

  <section class="page page--right">
    <div class="page-inner">
      <h2 class="section-title solutions-title">Our <span class="hl">Solutions</span></h2>
      <p>Norvale Advisory offers a full range of consultation services to help analyze your plant requirements for the effective implementation of solutions from our range of products. We cooperate with the end-user for a detailed analysis of the root cause and provide reliable solutions for different kinds of valve problems. Our products and services could be briefly divided into the following sections:</p>

      <h3 class="sub-title">New <span class="hl">Valves</span></h3>
      <p>We provide consultation on and design of a variety of valves for different kinds of industrial applications. We have a rich set of valve designs and solutions available, providing solutions for severe service applications. For special valve solutions not available in the market, we can help our clients by manufacturing and delivering those valves in the shortest possible timeframe under the most complicated requirements.</p>

      <h3 class="sub-title">Upgrade <span class="hl">Retrofit</span></h3>
      <p class="beside-photo">We supply highly reliable and efficient upgrading solutions for our clients, with the following key advantages:</p>
      <ul class="ticks beside-photo">
        <li><svg width="10" height="8" viewBox="0 0 10 8"><path d="M1 4l3 3 5-6" fill="none" stroke="#f0931e" stroke-width="1.4"/></svg>Fits well into the existing valve</li>
        <li><svg width="10" height="8" viewBox="0 0 10 8"><path d="M1 4l3 3 5-6" fill="none" stroke="#f0931e" stroke-width="1.4"/></svg>Full responsibility of the valve</li>
        <li><svg width="10" height="8" viewBox="0 0 10 8"><path d="M1 4l3 3 5-6" fill="none" stroke="#f0931e" stroke-width="1.4"/></svg>Detailed documentation</li>
        <li><svg width="10" height="8" viewBox="0 0 10 8"><path d="M1 4l3 3 5-6" fill="none" stroke="#f0931e" stroke-width="1.4"/></svg>Saves the cost of piping modifications</li>
        <li><svg width="10" height="8" viewBox="0 0 10 8"><path d="M1 4l3 3 5-6" fill="none" stroke="#f0931e" stroke-width="1.4"/></svg>Lower installation costs</li>
        <li><svg width="10" height="8" viewBox="0 0 10 8"><path d="M1 4l3 3 5-6" fill="none" stroke="#f0931e" stroke-width="1.4"/></svg>Shorter plant downtime</li>
      </ul>

      <h3 class="sub-title">Spare <span class="hl">Parts</span></h3>
      <p class="beside-photo">We are not only focus on providing reliable valves and upgrades, but also assist our clients in maintaining their valves. We provide direct OEM part replacements, with quality same as those originally installed. Other than providing common spare parts, we can also help in the replacement of obsolete parts not commonly available by using our trusted sources or our highly advanced reverse engineering techniques.</p>
      <p class="lead-accent">The advantages of using spare parts provided by us are as follows:</p>
      <ul class="ticks beside-photo">
        <li><svg width="10" height="8" viewBox="0 0 10 8"><path d="M1 4l3 3 5-6" fill="none" stroke="#f0931e" stroke-width="1.4"/></svg>Completely interchangeable</li>
        <li><svg width="10" height="8" viewBox="0 0 10 8"><path d="M1 4l3 3 5-6" fill="none" stroke="#f0931e" stroke-width="1.4"/></svg>Use of latest technology makes our parts highly reliable</li>
        <li><svg width="10" height="8" viewBox="0 0 10 8"><path d="M1 4l3 3 5-6" fill="none" stroke="#f0931e" stroke-width="1.4"/></svg>Lower costs</li>
        <li><svg width="10" height="8" viewBox="0 0 10 8"><path d="M1 4l3 3 5-6" fill="none" stroke="#f0931e" stroke-width="1.4"/></svg>Faster delivery</li>
      </ul>
    </div>
    <div class="photo photo--valve" role="img" aria-label="Photo of a large control valve with red actuator in a workshop"></div>
    <div class="photo photo--ring" role="img" aria-label="Photo of a machined metal seal ring"></div>
    <div class="photo photo--parts" role="img" aria-label="Photo of machined valve spare parts, stems and sleeves"></div>
  </section>
</main>
</body>
</html>
```